Lume Hart Co Need a custom graphic

I need to have the attached chart re-designed in a hand colored pencil format. The heading needs to be changed to "The most effective methods for hiring sales people". Do not include the background logo in the sample file.

Place the attached Lume Hart Co logo next to the most effective methods (91%)

```html
<!DOCTYPE html>
<html lang="en">
<head>
<meta charset="utf-8">
<title>The Most Effective Methods for Hiring Sales People</title>
<link href="https://fonts.googleapis.com/css2?family=Luckiest+Guy&family=Gochi+Hand&family=Poppins:wght@400;600;700&display=swap" rel="stylesheet">
<style>
  :root {
    --navy: #1d3a78;
    --navy-dark: #14264f;
    --sky: #3a8fd8;
    --ribbon: #2f9be0;
    --grid: #e3e3e3;
    --panel-grey: #f2f2f2;
    --muted: #9a9a9a;
    --ink: #333333;
    --arrow: #b8b8b8;
  }
  html, body { margin: 0; padding: 0; overflow: hidden; }
  body { width: 750px; height: 1200px; background: #ffffff; }
  .poster { display: block; width: 750px; height: 1200px; }
  .hand { font-family: "Gochi Hand", cursive; fill: var(--navy); }
  .hand-title { font-family: "Luckiest Guy", cursive; fill: #ffffff; letter-spacing: 0.5px; }
  .clean { font-family: "Poppins", sans-serif; fill: var(--ink); }
  .clean-strong { font-weight: 700; fill: var(--navy-dark); }
  .hand-strong { font-size: 12px; }
  .tick-label-hand { font-family: "Gochi Hand", cursive; fill: var(--navy); font-size: 10px; }
  .tick-label-clean { font-family: "Poppins", sans-serif; fill: var(--navy-dark); font-size: 9px; font-weight: 600; }
  .brand-name { font-family: "Poppins", sans-serif; font-weight: 600; fill: var(--navy); font-size: 14px; }
</style>
</head>
<body>
<svg class="poster" viewBox="0 0 640 1024" xmlns="http://www.w3.org/2000/svg">
  <defs>
    <marker id="arrowhead" viewBox="0 0 10 10" refX="8" refY="5" markerWidth="5" markerHeight="5" orient="auto-start-reverse">
      <path d="M0 0 L10 5 L0 10 z" fill="var(--arrow)"/>
    </marker>
  </defs>

  <!-- Hand-drawn panel -->
  <g class="panel-sketch">
    <rect x="0" y="0" width="640" height="510" fill="#ffffff"/>
    <path class="ribbon" d="M45 36 L595 36 L580 61 L597 86 L45 86 L60 61 Z" fill="var(--ribbon)" stroke="var(--navy)" stroke-width="2"/>
    <text class="hand-title" x="322" y="69" font-size="17" text-anchor="middle">THE MOST EFFECTIVE METHODS FOR HIRING SALES PEOPLE</text>

    <g class="grid" stroke="var(--grid)" stroke-width="1">
      <line x1="115" y1="134" x2="595" y2="134"/><line x1="115" y1="164" x2="595" y2="164"/>
      <line x1="115" y1="193" x2="595" y2="193"/><line x1="115" y1="223" x2="595" y2="223"/>
      <line x1="115" y1="252" x2="595" y2="252"/><line x1="115" y1="282" x2="595" y2="282"/>
      <line x1="115" y1="312" x2="595" y2="312"/><line x1="115" y1="341" x2="595" y2="341"/>
      <line x1="115" y1="371" x2="595" y2="371"/><line x1="115" y1="400" x2="595" y2="400"/>
      <line x1="115" y1="432" x2="595" y2="432"/>
      <line x1="115" y1="134" x2="115" y2="432"/><line x1="158" y1="134" x2="158" y2="432"/>
      <line x1="201" y1="134" x2="201" y2="432"/><line x1="244" y1="134" x2="244" y2="432"/>
      <line x1="287" y1="134" x2="287" y2="432"/><line x1="330" y1="134" x2="330" y2="432"/>
      <line x1="373" y1="134" x2="373" y2="432"/><line x1="416" y1="134" x2="416" y2="432"/>
      <line x1="459" y1="134" x2="459" y2="432"/><line x1="502" y1="134" x2="502" y2="432"/>
      <line x1="545" y1="134" x2="545" y2="432"/><line x1="595" y1="134" x2="595" y2="432"/>
    </g>

    <g class="tick-label-hand" text-anchor="end">
      <text x="100" y="137">1.00</text><text x="100" y="167">0.90</text><text x="100" y="196">0.80</text>
      <text x="100" y="226">0.70</text><text x="100" y="255">0.60</text><text x="100" y="285">0.50</text>
      <text x="100" y="315">0.40</text><text x="100" y="344">0.30</text><text x="100" y="374">0.20</text>
      <text x="100" y="403">0.10</text><text x="100" y="433">0.00</text>
    </g>

    <text class="hand" x="58" y="285" font-size="15" text-anchor="middle" transform="rotate(-90 58 285)">Predictive Validity</text>
    <text class="hand" x="322" y="470" font-size="15" text-anchor="middle">Hiring Method</text>

    <polyline fill="none" stroke="var(--navy)" stroke-width="3" stroke-linejoin="round"
      points="158,393 201,380 244,375 287,375 330,362 373,362 416,338 459,282 502,263 545,221 592,163"/>
    <g fill="var(--sky)" stroke="var(--navy)" stroke-width="2">
      <circle cx="158" cy="393" r="5.5"/><circle cx="201" cy="380" r="5.5"/><circle cx="244" cy="375" r="5.5"/>
      <circle cx="287" cy="375" r="5.5"/><circle cx="330" cy="362" r="5.5"/><circle cx="373" cy="362" r="5.5"/>
      <circle cx="416" cy="338" r="5.5"/><circle cx="459" cy="282" r="5.5"/><circle cx="502" cy="263" r="5.5"/>
      <circle cx="545" cy="221" r="5.5"/><circle cx="592" cy="163" r="5.5"/>
    </g>

    <text class="brand-name" x="440" y="132" text-anchor="middle">Lume Hart Co</text>

    <g class="labels-hand hand" font-size="10.5">
      <text x="340" y="159">Sales-specific Multi-measurement Assessment, <tspan class="hand-strong">91%</tspan></text>
      <text x="353" y="205">Multi-measurement Assessment, <tspan class="hand-strong">71%</tspan></text>
      <text x="254" y="236">Highly Structured Interview With Scorecard, <tspan class="hand-strong">57%</tspan></text>
      <text x="297" y="270">General Mental Ability, <tspan class="hand-strong">51%</tspan></text>
      <text x="290" y="306">Reference Check, <tspan class="hand-strong">23%</tspan></text>
      <text x="168" y="334">Behavior/ Personality Test, <tspan class="hand-strong">20%</tspan></text>
      <text x="136" y="362">Resume, <tspan class="hand-strong">18%</tspan></text>
      <text x="131" y="431">Culture Test, <tspan class="hand-strong">13%</tspan></text>
      <text x="225" y="412">Traditional Interview, <tspan class="hand-strong">20%</tspan></text>
      <text x="355" y="409">Emotional Intelligence, <tspan class="hand-strong">23%</tspan></text>
      <text x="470" y="355">Skills Test, <tspan class="hand-strong">33%</tspan></text>
    </g>

    <g class="arrows" stroke="var(--arrow)" stroke-width="1.2" marker-end="url(#arrowhead)">
      <line x1="550" y1="157" x2="582" y2="161"/>
      <line x1="512" y1="211" x2="536" y2="217"/>
      <line x1="468" y1="240" x2="494" y2="256"/>
      <line x1="418" y1="268" x2="448" y2="279"/>
      <line x1="330" y1="310" x2="330" y2="352"/>
      <line x1="244" y1="338" x2="244" y2="366"/>
      <line x1="176" y1="366" x2="192" y2="376"/>
      <line x1="158" y1="420" x2="158" y2="403"/>
      <line x1="287" y1="400" x2="287" y2="385"/>
      <line x1="373" y1="396" x2="373" y2="372"/>
      <line x1="465" y1="350" x2="427" y2="340"/>
    </g>
  </g>

  <!-- Clean panel -->
  <g class="panel-clean">
    <rect x="0" y="512" width="640" height="512" fill="var(--panel-grey)"/>
    <text class="clean" x="35" y="578" font-size="20" font-weight="700" fill="var(--navy-dark)" style="fill:var(--navy-dark)">The Most Effective Methods</text>
    <text class="clean" x="35" y="603" font-size="20" font-weight="600" style="fill:var(--muted)">For Hiring Sales People</text>

    <g class="grid" stroke="#e0e0e0" stroke-width="1">
      <line x1="118" y1="648" x2="600" y2="648"/><line x1="118" y1="677" x2="600" y2="677"/>
      <line x1="118" y1="707" x2="600" y2="707"/><line x1="118" y1="736" x2="600" y2="736"/>
      <line x1="118" y1="765" x2="600" y2="765"/><line x1="118" y1="795" x2="600" y2="795"/>
      <line x1="118" y1="824" x2="600" y2="824"/><line x1="118" y1="853" x2="600" y2="853"/>
      <line x1="118" y1="882" x2="600" y2="882"/><line x1="118" y1="912" x2="600" y2="912"/>
      <line x1="118" y1="941" x2="600" y2="941"/>
      <line x1="118" y1="648" x2="118" y2="941"/><line x1="158" y1="648" x2="158" y2="941"/>
      <line x1="201" y1="648" x2="201" y2="941"/><line x1="244" y1="648" x2="244" y2="941"/>
      <line x1="288" y1="648" x2="288" y2="941"/><line x1="331" y1="648" x2="331" y2="941"/>
      <line x1="374" y1="648" x2="374" y2="941"/><line x1="417" y1="648" x2="417" y2="941"/>
      <line x1="460" y1="648" x2="460" y2="941"/><line x1="503" y1="648" x2="503" y2="941"/>
      <line x1="546" y1="648" x2="546" y2="941"/><line x1="600" y1="648" x2="600" y2="941"/>
    </g>

    <g class="tick-label-clean" text-anchor="end">
      <text x="100" y="651">1.00</text><text x="100" y="680">0.90</text><text x="100" y="710">0.80</text>
      <text x="100" y="739">0.70</text><text x="100" y="768">0.60</text><text x="100" y="798">0.50</text>
      <text x="100" y="827">0.40</text><text x="100" y="856">0.30</text><text x="100" y="885">0.20</text>
      <text x="100" y="915">0.10</text><text x="100" y="944">0.00</text>
    </g>

    <text class="clean" x="55" y="795" font-size="12" text-anchor="middle" transform="rotate(-90 55 795)" style="fill:var(--navy-dark)">Predictive Validity</text>
    <text class="clean" x="354" y="982" font-size="12" text-anchor="middle" style="fill:var(--navy-dark)">Hiring Method</text>

    <polyline fill="none" stroke="var(--navy-dark)" stroke-width="3" stroke-linejoin="round"
      points="158,906 201,891 244,885 288,885 331,874 374,874 417,851 460,796 503,775 546,734 592,677"/>
    <g fill="var(--navy-dark)">
      <circle cx="158" cy="906" r="4.5"/><circle cx="201" cy="891" r="4.5"/><circle cx="244" cy="885" r="4.5"/>
      <circle cx="288" cy="885" r="4.5"/><circle cx="331" cy="874" r="4.5"/><circle cx="374" cy="874" r="4.5"/>
      <circle cx="417" cy="851" r="4.5"/><circle cx="460" cy="796" r="4.5"/><circle cx="503" cy="775" r="4.5"/>
      <circle cx="546" cy="734" r="4.5"/><circle cx="592" cy="677" r="4.5"/>
    </g>

    <rect class="callout" x="350" y="604" width="225" height="86" rx="8" fill="#ffffff"/>
    <text class="brand-name" x="450" y="634" text-anchor="middle">Lume Hart Co</text>
    <g class="clean" font-size="9" text-anchor="middle">
      <text x="450" y="658">Sales-specific</text>
      <text x="450" y="671">Multi-measurement Assessment, <tspan class="clean-strong">91%</tspan></text>
    </g>

    <g class="labels-clean clean" font-size="9">
      <text x="345" y="718">Multi-measurement Assessment, <tspan class="clean-strong">71%</tspan></text>
      <text x="253" y="747">Highly Structured Interview With Scorecard, <tspan class="clean-strong">57%</tspan></text>
      <text x="296" y="781">General Mental Ability, <tspan class="clean-strong">51%</tspan></text>
      <text x="290" y="818">Reference Check, <tspan class="clean-strong">23%</tspan></text>
      <text x="170" y="848">Behavior/ Personality Test, <tspan class="clean-strong">20%</tspan></text>
      <text x="135" y="875">Resume, <tspan class="clean-strong">18%</tspan></text>
      <text x="132" y="941">Culture Test, <tspan class="clean-strong">13%</tspan></text>
      <text x="224" y="925">Traditional Interview, <tspan class="clean-strong">20%</tspan></text>
      <text x="356" y="921">Emotional Intelligence, <tspan class="clean-strong">23%</tspan></text>
      <text x="470" y="867">Skills Test, <tspan class="clean-strong">33%</tspan></text>
    </g>

    <g class="arrows" stroke="var(--arrow)" stroke-width="1.2" marker-end="url(#arrowhead)">
      <line x1="552" y1="671" x2="582" y2="675"/>
      <line x1="512" y1="722" x2="537" y2="730"/>
      <line x1="470" y1="752" x2="495" y2="768"/>
      <line x1="420" y1="782" x2="450" y2="792"/>
      <line x1="331" y1="823" x2="331" y2="865"/>
      <line x1="244" y1="852" x2="244" y2="877"/>
      <line x1="180" y1="878" x2="193" y2="887"/>
      <line x1="158" y1="930" x2="158" y2="915"/>
      <line x1="288" y1="914" x2="288" y2="895"/>
      <line x1="374" y1="908" x2="374" y2="884"/>
      <line x1="465" y1="862" x2="427" y2="853"/>
    </g>
  </g>
</svg>
</body>
</html>
```